Website for a health information tech company

I need a website for a new startup company, Lumivale, Inc. that specializes in healthcare information technology. Lumivale is a monitoring system that uses wearable sensors and predictive algorithms to detect when an elderly persons health is declining and triggers progressively higher levels of interventions.

The site needs to be very simple, elegant and initially will have minimal information as company and product is still under development and is in a stealth mode. I like the tandovix.com website as it has a "single page" look and feel with sliding vertical sections. Ideally the sections would be "Home", "Technology", "Customers", "News", "About Us" and "Contact Us". The contact us should have a contact form that gets sent to an email address.

I have a couple of example sites that my site should take inspiration from (tandovix.com and brimholtway.com). I would like a WordPress backend so I can easily update content so the winning design should be easily importable or setup into Wordpress.

Target Market(s)

Investors, Customers (Doctors, Patients, Health Insurance companies, Hospital directors)

Industry/Entity Type

Healthcare

Requirements
Must have
• top horizontal menu that gets repeated on each vertical slide. Should have animated vertical slides. Must be viewable on any device (iPad, Android Tablets) correctly and must render correctly on different screen sizes. Must be viewable in all popular browsers. Must work well with touchscreen devices such as iPad, iPhone, Android tablets and phones.
Must have a content management system backend such as WordPress so I can edit/update content and in future add additional sections, images etc.

See attached company logo so colors must be complimentary to the logo colors. Feel free to use the logo colors as web site theme colors if it makes sense.
Nice to have
• Nice subtle textured background like linen or leather.
Should not have
• Not looking for traditional web site design with nav bars on left etc
Should not feel like a traditional web site where you click a link and another page loads. It must be animated slide into a different section. No flash or any other technology that requires plug ins.

```html
<!DOCTYPE html>
<html lang="en">
<head>
<meta charset="utf-8">
<title>Lumivale</title>
<link href="https://fonts.googleapis.com/css2?family=Source+Sans+3:wght@400;600;700&display=swap" rel="stylesheet">
<style>
:root{
  --orange:#f26a1b;
  --orange-light:#f8893f;
  --orange-dark:#e55a0c;
  --text:#555;
  --text-soft:#777;
  --heading:#555;
  --hero-bg:#e8e8e8;
  --panel-bg:#efefef;
  --footer-bg:#ececec;
  --white:#fff;
  --green:#7cbd1e;
  --grey-btn:#7a7a7a;
  --social:#6a6a6a;
  --input-bg:#f1f1f1;
  --input-border:#d8d8d8;
}
*{margin:0;padding:0;box-sizing:border-box}
html,body{width:1200px;height:1019px;overflow:hidden;background:var(--white)}
body{position:relative;font-family:"Source Sans 3",sans-serif;color:var(--text)}
.abs{position:absolute}

/* header */
.brand{left:176px;top:66px;display:flex;align-items:center;gap:10px}
.brand-dot{width:26px;height:26px;border-radius:50%;background:var(--orange)}
.brand-name{font-size:26px;font-weight:600;color:var(--orange)}
.account-btn{top:49px;width:90px;height:31px;color:var(--white);font-size:14px;font-weight:600;text-align:center;line-height:31px;border-radius:2px}
.account-btn.login{left:896px;background:linear-gradient(#8c8c8c,#646464)}
.account-btn.demo{left:991px;background:linear-gradient(#8fcf2a,#6aab12)}
.main-nav{left:441px;top:95px;width:640px;height:48px;display:flex;background:linear-gradient(var(--orange-light),var(--orange-dark));border-radius:2px}
.main-nav a{color:var(--white);text-decoration:none;font-size:19px;line-height:46px;text-align:center;border-right:1px solid rgba(255,255,255,.35)}
.main-nav a:last-child{border-right:0}

/* hero */
.hero{left:0;top:143px;width:1200px;height:331px;background:var(--hero-bg)}
.slide-arrow{top:133px;width:33px;height:33px}
.hero-title{left:157px;top:94px;font-size:23px;line-height:30px;color:var(--heading);font-weight:400}
.hero-title span{color:var(--orange)}
.hero-text{left:158px;top:165px;width:420px;font-size:13px;line-height:20px;text-align:justify;color:var(--text)}
.hero-devices{left:636px;top:35px;width:367px;height:266px;border-radius:14px;background:linear-gradient(135deg,#2a2a2a,#0d0d0d 60%,#3a3a3a)}
.hero-devices::after{content:"";position:absolute;left:46px;top:32px;width:228px;height:190px;background:linear-gradient(#f7f7f7,#e4e8ec)}

/* features */
.feature{top:497px;width:300px;height:104px;background:var(--panel-bg)}
.feature-icon{position:absolute;left:16px;top:14px}
.feature h3{position:absolute;left:55px;top:14px;font-size:17px;font-weight:400;color:var(--orange)}
.feature p{position:absolute;left:55px;top:47px;width:230px;font-size:13px;line-height:20px;color:var(--text-soft)}

/* welcome */
.section-title{font-size:22px;font-weight:400;color:var(--heading)}
.section-title span{color:var(--orange)}
.welcome-devices{left:172px;top:681px;width:150px;height:124px;border-radius:8px;background:linear-gradient(135deg,#2b2b2b,#111 70%,#3a3a3a)}
.welcome-text{left:373px;top:664px;width:377px;font-size:13px;line-height:20px;text-align:justify}

/* contact */
.field{left:768px;width:300px;height:25px;background:var(--input-bg);border:1px solid var(--input-border);border-top:2px solid #c9c9c9;font-size:11px;color:#999;padding:5px 10px}
.submit{left:979px;top:766px;width:89px;height:25px;background:linear-gradient(var(--orange-light),var(--orange-dark));color:var(--white);font-weight:700;font-size:13px;text-align:center;line-height:25px;border-radius:2px}

/* partners */
.partners{left:130px;top:855px;width:940px;display:flex;justify-content:space-between;align-items:center}
.partner{font-size:17px;font-weight:600;color:#6b6b6b}

/* footer */
.footer{left:0;top:931px;width:1200px;height:88px;background:var(--footer-bg)}
.social{left:130px;top:27px;display:flex;gap:8px}
.social span{width:32px;height:32px;border-radius:50%;background:var(--social)}
.footer-nav{right:131px;top:16px;font-size:13px;color:var(--text);word-spacing:2px}
.footer-nav .sep{margin:0 14px}
.copyright{right:131px;top:46px;font-size:13px;color:var(--text)}
</style>
</head>
<body>

<header>
  <div class="abs brand"><span class="brand-dot"></span><span class="brand-name">Lumivale</span></div>
  <div class="abs account-btn login">LOGIN</div>
  <div class="abs account-btn demo">DEMO</div>
  <nav class="abs main-nav">
    <a href="#" style="width:92px">Home</a>
    <a href="#" style="width:139px">Technology</a>
    <a href="#" style="width:122px">Customers</a>
    <a href="#" style="width:112px">About Us</a>
    <a href="#" style="width:175px">Contact Us</a>
  </nav>
</header>

<section class="abs hero">
  <svg class="abs slide-arrow" style="left:84px" viewBox="0 0 33 33"><circle cx="16.5" cy="16.5" r="16" fill="#d2d2d2"/><path d="M19 9l-8 7.5 8 7.5M11 16.5h12" stroke="#fff" stroke-width="3.5" fill="none" stroke-linecap="round" stroke-linejoin="round"/></svg>
  <svg class="abs slide-arrow" style="left:1080px" viewBox="0 0 33 33"><circle cx="16.5" cy="16.5" r="16" fill="#d2d2d2"/><path d="M14 9l8 7.5-8 7.5M22 16.5H10" stroke="#fff" stroke-width="3.5" fill="none" stroke-linecap="round" stroke-linejoin="round"/></svg>
  <h1 class="abs hero-title"><span>Lumi</span>vale is a patent pending<br>monitoring system</h1>
  <p class="abs hero-text">Lorem Ipsum is simply dummy text of the printing and typesetting industry. Lorem Ipsum has been the industry's standard dummy text ever since the 1500s.Lorem Ipsum is simply dummy text of the printing and typesetting industry. Lorem Ipsum has been the industry's standard dummy text ever &nbsp;.Lorem Ipsum is simply dummy text of the printing and typesetting industry.</p>
  <div class="abs hero-devices" role="img" aria-label="Tablet and phone showing the monitoring dashboard"></div>
</section>

<section>
  <div class="abs feature" style="left:130px">
    <svg class="feature-icon" width="28" height="26" viewBox="0 0 28 26"><rect x="1" y="2" width="26" height="16" rx="1" fill="none" stroke="#bbb" stroke-width="2"/><rect x="11" y="19" width="6" height="4" fill="#bbb"/></svg>
    <h3>Monitoring System</h3>
    <p>Lorem Ipsum is simply dummy text of the printing and typesetting industry.</p>
  </div>
  <div class="abs feature" style="left:450px">
    <svg class="feature-icon" width="30" height="30" viewBox="0 0 30 30"><path d="M4 12a11 11 0 0 0 14 14z" fill="#bbb"/><path d="M16 8a8 8 0 0 1 6 6M17 3a13 13 0 0 1 10 10" stroke="#bbb" stroke-width="2" fill="none"/></svg>
    <h3>Our Technology</h3>
    <p>Lorem Ipsum is simply dummy text of the printing and typesetting industry.</p>
  </div>
  <div class="abs feature" style="left:768px">
    <svg class="feature-icon" width="24" height="28" viewBox="0 0 24 28"><rect x="2" y="1" width="20" height="26" rx="2" fill="none" stroke="#bbb" stroke-width="2"/><rect x="6" y="5" width="12" height="6" fill="#bbb"/><g fill="#bbb"><rect x="6" y="14" width="3" height="3"/><rect x="11" y="14" width="3" height="3"/><rect x="16" y="14" width="3" height="3"/><rect x="6" y="20" width="3" height="3"/><rect x="11" y="20" width="3" height="3"/><rect x="16" y="20" width="3" height="3"/></g></svg>
    <h3>Customer Care</h3>
    <p>Lorem Ipsum is simply dummy text of the printing and typesetting industry.</p>
  </div>
</section>

<section>
  <h2 class="abs section-title" style="left:130px;top:620px">Welcome to <span>Lumi</span>vale</h2>
  <div class="abs welcome-devices" role="img" aria-label="Tablet and phone showing the care app"></div>
  <p class="abs welcome-text">Lumivale is a patent pending monitoring system that uses wearable sensors and predictive algorithms to detect when an elderly persons health is declining and triggers progressively higher levels of interventions.The goal is to allow an elderly person, who often has 2 or more chronic conditions, to age in place and stay independent as long as possible by the use of &nbsp;intelligent monitoring to deliver just in time care.</p>
</section>

<section>
  <h2 class="abs section-title" style="left:767px;top:620px">Let’s be in touch</h2>
  <div class="abs field" style="top:670px">Name</div>
  <div class="abs field" style="top:702px">E-Mail ID</div>
  <div class="abs field" style="top:734px">Company /Organisations</div>
  <div class="abs submit">SUBMIT</div>
</section>

<div class="abs partners">
  <span class="partner">Norra</span>
  <span class="partner">Kelvane</span>
  <span class="partner">Tallowby</span>
  <span class="partner">Quessant</span>
  <span class="partner">Ovrelle</span>
  <span class="partner">Brinlo</span>
  <span class="partner">Pentaview</span>
  <span class="partner">Marrowind</span>
  <span class="partner">Holtgrave</span>
  <span class="partner">Vessamo</span>
</div>

<footer class="abs footer">
  <div class="abs social" aria-label="Social links"><span></span><span></span><span></span><span></span><span></span></div>
  <div class="abs footer-nav">Home<span class="sep">|</span>Technology<span class="sep">|</span>Customers<span class="sep">|</span>About Us<span class="sep">|</span>Contact Us</div>
  <div class="abs copyright">©2013 Lumivale | All Rights Reserved</div>
</footer>

</body>
</html>
```